KA VERLINE

We need a letterhead design for an Image & Etiquette Consultancy company based in Singapore.

The services we provide are Personal Image Consultation, Image & Etiquette Workshop for schools and corporate.

The design should have our corporate colour as seen in the logo files I have uploaded.

Since our company helps clients with their image, the design should be aesthetically very appealing. It should reflect a very classy & elegant feel.

I will print the letterhead using my printer but most of the time will use it to write letters to my clients therefore the format should include MS Word.

```html
<!DOCTYPE html>
<html lang="en">
<head>
<meta charset="utf-8">
<title>KA VERLINE Letterhead</title>
<link href="https://fonts.googleapis.com/css2?family=Questrial&family=Didact+Gothic&display=swap" rel="stylesheet">
<style>
  :root {
    --backdrop: #c9c4cc;
    --paper: #f2f2f2;
    --ink: #4a4a4a;
    --ink-dark: #2b2b2b;
    --plum: #3a2346;
    --gold-start: #b8891f;
    --gold-end: #e6bd2e;
    --signature-ink: #6a7cc4;
  }
  html, body {
    margin: 0;
    width: 1200px;
    height: 1000px;
    overflow: hidden;
    background: var(--backdrop);
  }
  .letterhead {
    position: absolute;
    left: 290px;
    top: 63px;
    width: 622px;
    height: 880px;
    background: var(--paper);
    font-family: "Didact Gothic", "Questrial", sans-serif;
    color: var(--ink);
  }
  .brand-name {
    position: absolute;
    left: 58px;
    top: 54px;
    margin: 0;
    font-family: "Questrial", sans-serif;
    font-weight: 400;
    font-size: 31px;
    letter-spacing: 0.5px;
    color: var(--plum);
    line-height: 1;
  }
  .contact {
    position: absolute;
    right: 59px;
    top: 58px;
    text-align: right;
    font-size: 10px;
    line-height: 12px;
    color: var(--ink-dark);
    font-style: normal;
  }
  .contact strong { color: var(--plum); }
  .letter-body {
    position: absolute;
    left: 58px;
    top: 289px;
    width: 505px;
    font-size: 9.6px;
    line-height: 11px;
  }
  .salutation {
    margin: 0 0 12px;
    font-weight: 700;
    color: var(--ink-dark);
  }
  .letter-body p.paragraph {
    margin: 0 0 11px;
    text-align: justify;
  }
  .sign-off {
    position: absolute;
    left: 58px;
    top: 563px;
    font-size: 9.6px;
    line-height: 11px;
  }
  .sign-off .name { font-weight: 700; color: var(--ink-dark); }
  .signature {
    position: absolute;
    left: 133px;
    top: 552px;
    width: 128px;
    height: 64px;
    background: var(--signature-ink);
    opacity: 0.18;
    border-radius: 4px;
  }
  .footer-band {
    position: absolute;
    bottom: 0;
    left: 0;
    width: 622px;
    height: 14px;
  }
</style>
</head>
<body>
  <main class="letterhead">
    <h1 class="brand-name">KA VERLINE</h1>

    <address class="contact">
      18 Harbour Crest Road, Singapore 519302<br>
      <strong>Tel:</strong> +65-6000 4821 · <strong>Email:</strong> hello@kaverline.com<br>
      www.kaverline.com
    </address>

    <section class="letter-body">
      <p class="salutation">Dear sir,</p>
      <p class="paragraph">Communication is a very integral part of living creatures, animals and humans. Communication may be verbal or written. Written communication however is only applicable to human beings. Can you even imagine a world without communication? Verbal communication can be through telephones, webcams or in person. Written communication is through letters, emails and mobile phone messages.</p>
      <p class="paragraph">In today's world of great inventions and technology, letters have somehow become redundant. It is the time for text messages or chats. But they still can communicate a lot more than all other modes of communication. Organizations and various government departments still bank on letters as a strong medium of communication. There is no comparison in costs of sending letters as compared to costs of mobile phone messages though – letters are far cheaper. Letters now commonly known as "hard copy documents" are considered more relevant and important than email copies of text messages as proof or evidence of some sort.</p>
      <p class="paragraph">Letters speak volumes about a person or an organization that writes it. So one must take utmost care ensuring that the language used in any letter is appropriate for the occasion for which it is being written. Since a letter is also a written proof or document, if there are certain things that should not form a part of it, then that too should be carefully handled.</p>
      <p class="paragraph">Writing a good letter is an art. But if for some reason someone is unable to write that perfect letter, these different types of letters provide a base for you to build on. Sample letters have been given for everyone to understand what all information needs to form a part of the letter type and then it can be customized.</p>
    </section>

    <div class="sign-off">
      Yours Sincerely,<br>
      <span class="name">Lorel Vensant</span>
    </div>
    <div class="signature" role="img" aria-label="Handwritten signature of the sender"></div>

    <svg class="footer-band" viewBox="0 0 622 14" aria-hidden="true">
      <defs>
        <linearGradient id="goldBand" x1="0" x2="1" y1="0" y2="0">
          <stop offset="0" stop-color="var(--gold-start)"/>
          <stop offset="1" stop-color="var(--gold-end)"/>
        </linearGradient>
      </defs>
      <rect x="0" y="0" width="445" height="14" fill="var(--plum)"/>
      <rect x="450" y="0" width="172" height="14" fill="url(#goldBand)"/>
    </svg>
  </main>
</body>
</html>
```